Consulting Company needs business card design

We need a business card design for a new consulting and business solutions company based in Marlow Isles called Corvale Partners Limited. Looking for a double sided business card with one side only including the company logo thats attached and the other including contact information. Logo contains blue and turquoise colors and is fine to be on both sides of the card.
Contact Information for Business Card
Corvale Partners Limited
P.O. Box HM318
Keelhaven KH 07
Marlow Isles
Name: Marcus Pellegrin
Position: Director
Telephone: 1 441 733 4906
Email: mpellegrin@corvale.example
Website: www.corvale.example

```html
<!DOCTYPE html>
<html lang="en">
<head>
<meta charset="utf-8">
<title>Corvale Partners Limited – Business Card</title>
<link rel="stylesheet" href="https://fonts.googleapis.com/css2?family=Lato:wght@300;400;700;900&display=swap">
<style>
  :root {
    --page-bg: #e9ecef;
    --card-white: #ffffff;
    --card-grey: #e3e6ea;
    --brand-blue: #1a8fd8;
    --back-top: #2db4e2;
    --back-bottom: #1476cf;
    --ink-light: #ffffff;
    --ink-soft: rgba(255,255,255,0.85);
  }
  * { box-sizing: border-box; margin: 0; padding: 0; }
  html, body { width: 1200px; height: 1200px; overflow: hidden; }
  body {
    background: var(--page-bg);
    font-family: "Lato", sans-serif;
    position: relative;
  }
  .card {
    position: absolute;
    left: 250px;
    width: 700px;
    height: 400px;
    border-radius: 4px;
    box-shadow: 0 10px 30px rgba(0,0,0,0.15);
    overflow: hidden;
  }
  .card-front {
    top: 120px;
    background: linear-gradient(160deg, var(--card-grey) 0%, var(--card-white) 45%, var(--card-white) 70%, var(--card-grey) 100%);
    display: flex;
    align-items: center;
    justify-content: center;
  }
  .brand-lockup { display: flex; align-items: center; gap: 22px; }
  .brand-dot {
    width: 64px; height: 64px; border-radius: 50%;
    background: var(--brand-blue);
  }
  .brand-name {
    font-weight: 700; font-size: 40px;
    color: var(--brand-blue); letter-spacing: 0.5px;
  }
  .card-back {
    top: 640px;
    background: linear-gradient(180deg, var(--back-top) 0%, var(--back-bottom) 100%);
    color: var(--ink-light);
    padding: 44px 0 0 56px;
  }
  .back-decoration {
    position: absolute;
    right: -40px; bottom: -40px;
    width: 300px; height: 300px;
    border-radius: 50%;
    background: rgba(255,255,255,0.1);
  }
  .company-line { font-weight: 700; font-size: 26px; }
  .rule {
    width: 300px; height: 2px;
    background: var(--ink-soft);
    margin: 14px 0 12px;
  }
  .person-name { font-size: 32px; letter-spacing: 1px; text-transform: uppercase; }
  .person-name .first { font-weight: 900; }
  .person-name .last { font-weight: 300; }
  .person-role { font-size: 15px; font-weight: 400; color: var(--ink-soft); margin-top: 2px; }
  .contact-list { list-style: none; margin-top: 6px; }
  .contact-item {
    display: flex; align-items: flex-start; gap: 12px;
    font-size: 19px; line-height: 1.55;
  }
  .contact-item svg { flex: none; margin-top: 6px; }
  .contact-item .address { font-size: 17px; line-height: 1.4; padding-top: 3px; }
</style>
</head>
<body>
  <section class="card card-front" aria-label="Business card front">
    <div class="brand-lockup">
      <span class="brand-dot"></span>
      <span class="brand-name">Corvale Partners Limited</span>
    </div>
  </section>

  <section class="card card-back" aria-label="Business card back">
    <div class="back-decoration"></div>
    <p class="company-line">Corvale Partners Limited</p>
    <div class="rule"></div>
    <p class="person-name"><span class="first">Marcus</span> <span class="last">Pellegrin</span></p>
    <p class="person-role">Director</p>
    <div class="rule"></div>
    <ul class="contact-list">
      <li class="contact-item">
        <svg width="18" height="18" viewBox="0 0 18 18" fill="none" stroke="#fff" stroke-width="1.4"><circle cx="9" cy="9" r="8"/><path d="M6 5.2l1.4 1.6-.8 1.1c.5 1 1.3 1.8 2.3 2.3l1.1-.8 1.6 1.4-.9 1.2c-2.6-.4-4.7-2.5-5.1-5.1z"/></svg>
        <span>1 441 733 4906</span>
      </li>
      <li class="contact-item">
        <svg width="18" height="18" viewBox="0 0 18 18" fill="none" stroke="#fff" stroke-width="1.4"><circle cx="9" cy="9" r="8"/><rect x="5" y="6.2" width="8" height="5.6"/><path d="M5 6.4l4 3 4-3"/></svg>
        <span>mpellegrin@corvale.example</span>
      </li>
      <li class="contact-item">
        <svg width="18" height="18" viewBox="0 0 18 18" fill="none" stroke="#fff" stroke-width="1.4"><circle cx="9" cy="9" r="8"/><circle cx="9" cy="9" r="4.5"/><path d="M4.5 9h9M9 4.5c-1.6 1.3-1.6 7.7 0 9M9 4.5c1.6 1.3 1.6 7.7 0 9"/></svg>
        <span>www.corvale.example</span>
      </li>
      <li class="contact-item">
        <svg width="18" height="18" viewBox="0 0 18 18" fill="none" stroke="#fff" stroke-width="1.4"><circle cx="9" cy="9" r="8"/><path d="M9 13.5s-3-3-3-5.3a3 3 0 016 0c0 2.3-3 5.3-3 5.3z"/><circle cx="9" cy="8.2" r="1"/></svg>
        <span class="address">P.O. Box HM318, Keelhaven KH 07<br>Marlow Isles</span>
      </li>
    </ul>
  </section>
</body>
</html>
```